Design Home Page Elements

Looking for a concept and 9 images for a box-type home page that displays 8 products and a 'request demo' call to action. Task includes refining the page layout and design of 9 images (logo + 8 products). See attached file for mock-up.
The logo and images shown in the mock-up show all the elements I am looking for - but I would like them rendered in a cleaner, more minimalist style (more like Vorla).
For starters, please just present your rendition of the logo and a single product and I will let you know if you are on the right track. Please feel free to use a different color scheme.
Target Market(s)
B2B. Target market for this product will be technology aware businesses.
Industry/Entity Type
Call

```html
<!DOCTYPE html>
<html lang="en">
<head>
<meta charset="utf-8">
<title>Nimbus Relay – The Ultimate White Label Communications Platform</title>
<link rel="stylesheet" href="https://fonts.googleapis.com/css2?family=Source+Sans+3:wght@400;600;700&display=swap">
<style>
  :root {
    --ink: #173a44;
    --teal: #6ccac4;
    --teal-light: #c9ece9;
    --teal-dark: #4fb3ad;
    --nav-top: #a9e0dc;
    --nav-bottom: #5fbfb8;
    --paper: #ffffff;
    --search-border: #8fd3ce;
    --go: #7a7a7a;
  }
  * { box-sizing: border-box; margin: 0; padding: 0; }
  html, body { width: 898px; height: 1200px; overflow: hidden; background: var(--paper); }
  body { position: relative; font-family: "Source Sans 3", "Myriad Pro", Arial, sans-serif; color: var(--ink); }

  .brand {
    position: absolute; left: 48px; top: 58px;
    display: flex; align-items: center; gap: 10px;
    font-size: 36px; font-weight: 700; color: var(--teal); letter-spacing: -0.5px;
  }
  .brand-dot { width: 22px; height: 22px; border-radius: 50%; background: var(--teal); }

  .main-nav {
    position: absolute; left: 315px; top: 75px; width: 570px; height: 24px;
    display: flex; border: 1px solid var(--teal-dark);
    background: linear-gradient(var(--nav-top), var(--nav-bottom));
  }
  .main-nav a {
    display: block; height: 100%; text-align: center; text-decoration: none;
    color: var(--paper); font-size: 18px; line-height: 22px;
    border-right: 2px solid var(--paper);
  }
  .main-nav a:nth-child(1) { width: 86px; }
  .main-nav a:nth-child(2) { width: 88px; }
  .main-nav a:nth-child(3) { width: 88px; }
  .main-nav a:nth-child(4) { width: 88px; }
  .main-nav a:nth-child(5) { width: 78px; border-right: none; }
  .search { display: flex; align-items: center; flex: 1; padding: 2px 2px 2px 0; }
  .search-field { flex: 1; height: 16px; background: var(--paper); border: 1px solid var(--search-border); }
  .search-go {
    width: 20px; height: 16px; background: var(--go); color: var(--paper);
    font-size: 9px; line-height: 16px; text-align: center;
  }

  .page-title {
    position: absolute; left: 0; width: 886px; top: 204px; text-align: center;
    font-size: 31px; font-weight: 600; letter-spacing: -0.6px;
  }

  .product-grid {
    position: absolute; left: 138px; top: 289px; width: 612px; height: 503px;
    border: 3px solid var(--ink);
  }
  .product {
    position: absolute; width: 200px; text-align: center; text-decoration: none; color: var(--ink);
  }
  .product svg { display: block; margin: 0 auto; }
  .product-name { display: block; margin-top: 22px; font-size: 17px; font-weight: 700; letter-spacing: -0.4px; }

  .feature-band {
    position: absolute; left: 75px; top: 862px; width: 748px; height: 294px; background: var(--ink);
  }
</style>
</head>
<body>
  <svg width="0" height="0" style="position:absolute">
    <defs>
      <linearGradient id="orb" x1="0" y1="0" x2="0" y2="1">
        <stop offset="0" stop-color="#d8f2f0"/>
        <stop offset="0.55" stop-color="#8ed6d0"/>
        <stop offset="1" stop-color="#5ec3bc"/>
      </linearGradient>
      <g id="share-icon">
        <circle cx="36" cy="36" r="34" fill="#e8e8e8"/>
        <circle cx="36" cy="36" r="31" fill="url(#orb)"/>
        <rect x="20" y="26" width="30" height="21" rx="4" fill="none" stroke="#fff" stroke-width="4"/>
        <path d="M30 39 C32 30 38 27 46 27 L46 22 L55 30 L46 37 L46 32 C40 32 34 34 30 39 Z" fill="#fff"/>
      </g>
    </defs>
  </svg>

  <header>
    <div class="brand"><span class="brand-dot"></span>Nimbus Relay</div>
    <nav class="main-nav">
      <a href="#">About</a>
      <a href="#">Services</a>
      <a href="#">Support</a>
      <a href="#">Contact</a>
      <a href="#">Blog</a>
      <div class="search"><span class="search-field"></span><span class="search-go">Go</span></div>
    </nav>
  </header>

  <h1 class="page-title">The Ultimate White Label Communications Platform</h1>

  <section class="product-grid">
    <a class="product" href="#" style="left:18px;top:44px"><svg width="72" height="72"><use href="#share-icon"/></svg><span class="product-name">Hosted PBX</span></a>
    <a class="product" href="#" style="left:200px;top:44px"><svg width="72" height="72"><use href="#share-icon"/></svg><span class="product-name">Web Conferencing</span></a>
    <a class="product" href="#" style="left:386px;top:44px"><svg width="72" height="72"><use href="#share-icon"/></svg><span class="product-name">Instant Messaging</span></a>
    <a class="product" href="#" style="left:18px;top:187px"><svg width="72" height="72"><use href="#share-icon"/></svg><span class="product-name">Mobile Apps</span></a>
    <a class="product" href="#" style="left:200px;top:187px"><svg width="72" height="72"><use href="#share-icon"/></svg><span class="product-name">Customer OnBoarding</span></a>
    <a class="product" href="#" style="left:386px;top:187px"><svg width="72" height="72"><use href="#share-icon"/></svg><span class="product-name">Billing and CRM</span></a>
    <a class="product" href="#" style="left:18px;top:329px"><svg width="72" height="72"><use href="#share-icon"/></svg><span class="product-name">DID Management</span></a>
    <a class="product" href="#" style="left:200px;top:329px"><svg width="72" height="72"><use href="#share-icon"/></svg><span class="product-name">LCR</span></a>
    <a class="product" href="#" style="left:386px;top:329px"><svg width="72" height="72"><use href="#share-icon"/></svg><span class="product-name">Request a Demo</span></a>
  </section>

  <section class="feature-band" aria-label="Feature area"></section>
</body>
</html>
```